Business Card Design

building company specialistloft conversion,extension ,bathrooms ,kitchens ,painting and decorating all general building work

Industry/Entity Type

Building

Contact Information for Business Card

K&M Property renovation Ltd
tel -07914638205
email-Mdorin07@brixmail.net
web in progres

Font styles to use
Sans Serif

Requirements
Must have
• name of the company
• all contact details
Nice to have
• some of the skills

```html
<!DOCTYPE html>
<html lang="en">
<head>
<meta charset="utf-8">
<title>K&amp;M Property renovation – Business Card</title>
<link href="https://fonts.googleapis.com/css2?family=Lato:wght@300;400;700;900&display=swap" rel="stylesheet">
<style>
  :root {
    --stage-light: #dcdcdc;
    --stage-dark: #8e8e8e;
    --card-dark: #2a2a2c;
    --card-mid: #313133;
    --band-grey: #59595b;
    --tab-grey: #6b6b6d;
    --ink-white: #ffffff;
    --ink-soft: #c4c4c4;
    --ink-muted: #a9a9ab;
  }
  * { box-sizing: border-box; margin: 0; padding: 0; }
  html, body { width: 1200px; height: 800px; overflow: hidden; }
  body {
    background: radial-gradient(ellipse at 50% 45%, var(--stage-light) 0%, var(--stage-dark) 100%);
    font-family: "Lato", Arial, sans-serif;
    position: relative;
  }
  .card {
    position: absolute;
    top: 245px;
    width: 500px;
    height: 310px;
    background: var(--card-dark);
    overflow: hidden;
    box-shadow: 0 10px 24px rgba(0,0,0,0.35);
  }
  .card--front { left: 70px; }
  .card--back { left: 630px; }

  /* front */
  .front__lower {
    position: absolute; left: 0; right: 0; top: 188px; bottom: 0;
    background: var(--card-mid);
  }
  .stitch {
    position: absolute; left: 0; right: 0; height: 0;
    border-top: 1.5px dashed var(--ink-white);
  }
  .front__stitch { top: 188px; }
  .brand { position: absolute; color: var(--ink-white); }
  .brand__name { font-weight: 900; line-height: 1; letter-spacing: 1px; }
  .brand__tagline { font-weight: 700; line-height: 1; }
  .front__brand { left: 100px; top: 34px; }
  .front__brand .brand__name { font-size: 86px; }
  .front__brand .brand__tagline { font-size: 19px; margin: 4px 0 0 22px; }
  .slogan {
    position: absolute; right: 26px; top: 148px;
    padding: 4px 14px;
    border: 1.5px dashed var(--ink-white);
    border-radius: 16px;
    background: var(--card-dark);
    color: var(--ink-soft);
    font-size: 15px; font-weight: 300;
    white-space: nowrap;
  }
  .name-band {
    position: absolute; left: 0; right: 0; top: 245px; height: 40px;
    background: var(--band-grey);
  }
  .name-tab {
    position: absolute; left: 0; top: 222px; width: 240px; height: 63px;
    background: var(--tab-grey);
    border-top-right-radius: 10px;
    padding: 28px 0 0 30px;
  }
  .person__name { color: var(--ink-soft); font-weight: 300; font-size: 17px; line-height: 1; white-space: nowrap; }
  .person__role { color: var(--ink-white); font-weight: 900; font-size: 8px; letter-spacing: 1px; margin-top: 2px; }

  /* back */
  .back__brand { right: 18px; top: 16px; text-align: left; }
  .back__brand .brand__name { font-size: 24px; }
  .back__brand .brand__tagline { font-size: 6px; font-weight: 400; margin-top: 1px; }
  .contact { position: absolute; left: 0; display: flex; align-items: center; }
  .contact--phone { top: 106px; }
  .contact--email { top: 148px; }
  .contact__lead { width: 42px; border-top: 1.5px dashed var(--ink-white); }
  .contact__icon {
    width: 36px; height: 26px;
    border: 1.5px dashed var(--ink-white); border-radius: 13px;
    display: flex; align-items: center; justify-content: center;
  }
  .contact__text { color: var(--ink-white); font-size: 17px; margin-left: 14px; letter-spacing: 0.3px; white-space: nowrap; }
  .back__band {
    position: absolute; left: 0; right: 0; top: 236px; height: 46px;
    background: var(--band-grey);
  }
  .back__band-stitch { top: 259px; }
  .mark-circle {
    position: absolute; left: 22px; top: 242px; width: 34px; height: 34px;
    border-radius: 50%; border: 1.5px dashed var(--ink-white);
    background: var(--band-grey);
  }
  .company-line {
    position: absolute; left: 110px; top: 240px; width: 150px;
    text-align: center; color: var(--ink-white);
    font-size: 9px; line-height: 1.3;
    background: var(--band-grey);
    white-space: nowrap;
  }
  .back__name-tab {
    position: absolute; right: 14px; top: 212px; width: 210px; height: 52px;
    background: var(--tab-grey); border-radius: 9px;
    padding: 10px 0 0 22px;
  }
  .back__name-tab .person__name { font-size: 18px; }
  .back__name-tab .person__role { text-align: right; margin-right: 20px; }
</style>
</head>
<body>

<section class="card card--front" aria-label="Business card front">
  <div class="front__lower"></div>
  <div class="stitch front__stitch"></div>
  <div class="brand front__brand">
    <div class="brand__name">K&amp;M</div>
    <div class="brand__tagline">Property renovation</div>
  </div>
  <div class="slogan">Decorate Your Home.</div>
  <div class="name-band"></div>
  <div class="name-tab">
    <div class="person__name">Marek Dorinski</div>
    <div class="person__role">OWNER</div>
  </div>
</section>

<section class="card card--back" aria-label="Business card back">
  <div class="brand back__brand">
    <div class="brand__name">K&amp;M</div>
    <div class="brand__tagline">Property renovation</div>
  </div>

  <div class="contact contact--phone">
    <span class="contact__lead"></span>
    <span class="contact__icon">
      <svg width="10" height="16" viewBox="0 0 10 16" aria-hidden="true">
        <rect x="1" y="1" width="8" height="14" rx="1.5" fill="none" stroke="#fff" stroke-width="1.2"/>
        <line x1="4" y1="12.5" x2="6" y2="12.5" stroke="#fff" stroke-width="1.2"/>
      </svg>
    </span>
    <span class="contact__text">07914638205</span>
  </div>

  <div class="contact contact--email">
    <span class="contact__lead"></span>
    <span class="contact__icon">
      <svg width="16" height="16" viewBox="0 0 16 16" aria-hidden="true">
        <circle cx="8" cy="8" r="6.5" fill="none" stroke="#fff" stroke-width="1.2"/>
        <ellipse cx="8" cy="8" rx="3" ry="6.5" fill="none" stroke="#fff" stroke-width="1"/>
        <line x1="1.5" y1="8" x2="14.5" y2="8" stroke="#fff" stroke-width="1"/>
      </svg>
    </span>
    <span class="contact__text">email-Mdorin07@brixmail.net</span>
  </div>

  <div class="back__band"></div>
  <div class="stitch back__band-stitch"></div>
  <div class="mark-circle"></div>
  <div class="company-line">K&amp;M<br>Property Renovation Ltd</div>
  <div class="back__name-tab">
    <div class="person__name">Marek Dorinski</div>
    <div class="person__role">OWNER</div>
  </div>
</section>

</body>
</html>
```